SNACKS packaging uplift

We need to revamp the current popcorn design to a new more elegant , more premium and cleaner design. The new design should have allow the consumer to immediatly relate the new pack to the old design, and not think its a totally new brand. feel free to update the logo, product shots, but we would like to maintain the WHITE identity somehow.

```html
<!DOCTYPE html>
<html lang="en">
<head>
<meta charset="UTF-8">
<title>Kernelo Popcorn – Nacho Cheese Pack</title>
<link href="https://fonts.googleapis.com/css2?family=Anton&family=Yesteryear&display=swap" rel="stylesheet">
<style>
  :root {
    --bg-brown: #8a3d10;
    --bag-orange: #f7a21e;
    --bag-orange-light: #fbb437;
    --bag-orange-deep: #ef9410;
    --crimp-line: #ffc75a;
    --label-rust: #b9573b;
    --label-rust-light: #c4634a;
    --brand-red: #c8262b;
    --white: #ffffff;
    --popcorn-gold: #e4a44a;
    --bowl-grey: #e8e6e1;
  }
  * { box-sizing: border-box; margin: 0; padding: 0; }
  html, body {
    width: 1200px;
    height: 933px;
    overflow: hidden;
    background: var(--bg-brown);
  }
  .canvas {
    position: relative;
    width: 1200px;
    height: 933px;
    background: var(--bg-brown);
  }
  .pack {
    position: absolute;
    left: 340px;
    top: 50px;
    width: 520px;
    height: 833px;
    background: linear-gradient(160deg, var(--bag-orange-light) 0%, var(--bag-orange) 45%, var(--bag-orange-deep) 100%);
    border-radius: 6px;
    overflow: hidden;
  }
  .pack__crimp {
    position: absolute;
    left: 0;
    width: 100%;
    height: 44px;
  }
  .pack__crimp--top { top: 0; }
  .pack__crimp--bottom { bottom: 0; }
  .pack__brand {
    position: absolute;
    top: 120px;
    left: 0;
    width: 100%;
    display: flex;
    align-items: center;
    justify-content: center;
    gap: 14px;
  }
  .pack__brand-dot {
    width: 34px;
    height: 34px;
    border-radius: 50%;
    background: var(--white);
  }
  .pack__brand-name {
    font-family: "Anton", sans-serif;
    font-size: 54px;
    letter-spacing: 2px;
    color: var(--white);
    line-height: 1;
  }
  .pack__label {
    position: absolute;
    left: 70px;
    top: 300px;
    width: 380px;
    height: 440px;
  }
  .pack__label-shape {
    position: absolute;
    inset: 0;
  }
  .pack__title {
    position: absolute;
    left: 0;
    top: 78px;
    width: 100%;
    text-align: center;
    font-family: "Anton", sans-serif;
    font-size: 128px;
    line-height: 0.98;
    color: var(--white);
    letter-spacing: 1px;
  }
  .pack__flavour {
    position: absolute;
    left: 0;
    top: 330px;
    width: 100%;
    text-align: center;
    font-family: "Yesteryear", cursive;
    font-size: 40px;
    line-height: 0.95;
    color: var(--white);
  }
  .photo {
    position: absolute;
  }
  .photo--cluster-top {
    left: 20px;
    top: 380px;
    width: 110px;
    height: 100px;
    border-radius: 46% 54% 50% 50%;
    background: radial-gradient(circle at 40% 40%, #f3cd8e, var(--popcorn-gold));
  }
  .photo--bowl {
    left: 360px;
    top: 380px;
    width: 130px;
    height: 90px;
    border-radius: 14px 14px 60px 60px;
    background: linear-gradient(180deg, #d88a45 0%, #d88a45 30%, var(--bowl-grey) 31%, #cfccc5 100%);
  }
  .photo--cluster-bottom {
    left: 70px;
    top: 650px;
    width: 80px;
    height: 80px;
    border-radius: 50% 45% 52% 48%;
    background: radial-gradient(circle at 40% 40%, #f3cd8e, var(--popcorn-gold));
  }
</style>
</head>
<body>
<main class="canvas">
  <section class="pack">
    <svg class="pack__crimp pack__crimp--top" viewBox="0 0 520 44" preserveAspectRatio="none">
      <rect width="520" height="44" fill="#f59c18"/>
      <g stroke="var(--crimp-line)" stroke-width="3">
        <line x1="0" y1="10" x2="520" y2="10"/>
        <line x1="0" y1="18" x2="520" y2="18"/>
        <line x1="0" y1="26" x2="520" y2="26"/>
        <line x1="0" y1="34" x2="520" y2="34"/>
      </g>
    </svg>

    <div class="pack__brand">
      <span class="pack__brand-dot"></span>
      <span class="pack__brand-name">KERNELO</span>
    </div>

    <div class="pack__label">
      <svg class="pack__label-shape" viewBox="0 0 380 440" preserveAspectRatio="none">
        <path d="M40 0 H340 Q340 40 380 40 V400 Q340 400 340 440 H40 Q40 400 0 400 V40 Q40 40 40 0 Z" fill="var(--label-rust)"/>
      </svg>
      <h1 class="pack__title">POP<br>CORN</h1>
      <p class="pack__flavour">Nacho Cheese<br>Flavour</p>
    </div>

    <div class="photo photo--cluster-top" role="img" aria-label="Caramel-coated popcorn cluster"></div>
    <div class="photo photo--bowl" role="img" aria-label="White bowl filled with nacho cheese popcorn"></div>
    <div class="photo photo--cluster-bottom" role="img" aria-label="Small caramel popcorn cluster"></div>

    <svg class="pack__crimp pack__crimp--bottom" viewBox="0 0 520 44" preserveAspectRatio="none">
      <rect width="520" height="44" fill="#f59c18"/>
      <g stroke="var(--crimp-line)" stroke-width="3">
        <line x1="0" y1="10" x2="520" y2="10"/>
        <line x1="0" y1="18" x2="520" y2="18"/>
        <line x1="0" y1="26" x2="520" y2="26"/>
        <line x1="0" y1="34" x2="520" y2="34"/>
      </g>
    </svg>
  </section>
</main>
</body>
</html>
```